Corvel Lending Systems Re-design.

Quenvora have recently launched a new site using Brickloft CMS system (http://www.corvellendingsystems.example.com.au). We are looking to update the look and feel to match the rest of our brands (http://www.velnarix.example.com.au and http://www.tidelark.example.com.au) We are keen for the design to be more visually engaging, incorporating more imagery and create a clean and easy to navigate interface.

We are looking for 2 pages to be designed. The first page would be the homepage which should contain the following:
Menu to the sub categories provided in the site map.
Room for latest news articles
Small area for polls
Contact us section
Page 2 should offer a content page. An example of this would be CRM (sales Platform) from the site map. This page would need to contain an overall description of the product and menu to the following:
Flash Demo.
Features and Benefits.
Enquire now.

Target Market(s)

Quenvora offer software and web tools that enable Mortgage brokers to manage their clients, choose the most applicable loan and submit applications to the lender (bank).
The target market for this site is mainly mortgage brokers and the banking industry (lenders, Brokerages and Aggregators of homeloans).
Mortgage brokers often work in small brokerages or are self employed running their business within the local community, alternatively they may own a franchise business such as Brindle Key Finance, ZOLT or Lender Harbour.

Industry/Entity Type

Software

Number of Pages Required

2 pages

Requirements
Must have
• Must suitably match the look and feel of our sister companies velnarix.example.com.au and tidelark.example.com.au and our group site corvelgroup.example.com.au.
Colour scheme should not differ from the base logo colours provided.
Should not have
• Although Quenvora offers mortgage software to brokers we do not sell homeloans or deal directly with buyers, therefore pictures of houses and a look you see from lenders is not what we are looking for. Our customers are Mortgage brokers and top tier banks.

```html
<!DOCTYPE html>
<html lang="en">
<head>
<meta charset="utf-8">
<title>Quenvora Lending Systems – Home and CRM pages</title>
<link href="https://fonts.googleapis.com/css2?family=Arimo:wght@400;700&display=swap" rel="stylesheet">
<style>
:root{
  --crimson:#b1063b;
  --blush:#ecc9d1;
  --ink:#111;
  --stage:#dcdcdc;
  --white:#fff;
}
*{box-sizing:border-box;margin:0;padding:0}
html,body{width:750px;height:1200px;overflow:hidden}
body{background:var(--stage);font-family:"Arimo",Arial,sans-serif;color:var(--ink)}
.stage{width:800px;height:1280px;position:relative;transform:scale(.9375);transform-origin:0 0;
  background:repeating-linear-gradient(135deg,#e4e4e4 0 3px,#d6d6d6 3px 5px)}
.divider{position:absolute;left:0;top:638px;width:800px;height:2px;background:var(--crimson)}
.page{position:absolute;left:80px;width:640px;height:604px;background:linear-gradient(#f7f7f7,#d9d9d9);border:1px solid #c9c9c9}
.page--home{top:18px}
.page--crm{top:658px}
.page > *{position:absolute}
.masthead{left:0;top:0;width:638px;height:83px;background:linear-gradient(#f5f5f5 0,#f5f5f5 45%,#e8b9c5 100%)}
.brand{left:25px;top:26px;display:flex;align-items:center;gap:8px;color:var(--crimson);font-weight:700;font-size:30px;letter-spacing:-.5px;line-height:30px}
.brand-mark{width:10px;height:10px;border-radius:50%;background:var(--crimson)}
.nav{left:2px;top:85px;display:flex;gap:3px}
.nav a{width:68px;height:22px;background:var(--crimson);color:var(--white);font-size:9.5px;font-weight:700;text-decoration:none;
  display:flex;align-items:center;justify-content:center;text-align:center;line-height:9px}
.nav a.is-active{background:var(--white);color:var(--crimson)}
.hero{left:15px;top:117px;width:610px;height:213px;border-radius:8px;background:linear-gradient(90deg,#f4f4f4,#e0e0e0);
  box-shadow:0 1px 4px rgba(0,0,0,.35);overflow:hidden}
.hero-photo{position:absolute;left:0;top:0;width:330px;height:213px;background:linear-gradient(120deg,#6d7f98 0%,#b9a99a 45%,#e3d7c7 70%,#3b3f4a 100%);border-right:2px solid var(--crimson)}
.hero-copy{position:absolute;left:355px;top:5px;width:252px;color:var(--crimson);font-weight:700}
.hero-copy h1{font-size:16px;margin-bottom:9px}
.hero-copy p{font-size:12.2px;line-height:15.5px;margin-bottom:15px}
.card{border-radius:7px;background:linear-gradient(#fafafa,#dcdcdc);box-shadow:0 1px 4px rgba(0,0,0,.35);overflow:hidden;font-size:9px;line-height:11px}
.card h2{height:32px;background:var(--crimson);color:var(--white);font-size:12.5px;display:flex;align-items:center;justify-content:center;border-radius:7px 7px 0 0}
.card .body{padding:6px 10px}
.card .body p{margin-bottom:8px}
.card-photo{height:67px}
.more{position:absolute;right:6px;bottom:5px;width:8px;height:8px;border-radius:50%;background:var(--crimson);color:#fff;font-size:8px;line-height:8px;text-align:center}
.card--contact{left:17px;top:370px;width:105px;height:160px}
.card--contact .body{padding:8px 10px;font-size:9.5px}
.card--facts{left:125px;top:357px;width:122px;height:185px}
.card--facts .card-photo{background:linear-gradient(#8fb0d4 0,#c7d5de 45%,#5b8b3c 60%,#b0533b 100%)}
.card--facts .body{padding:5px 10px 0}
.card--facts .body p{margin-bottom:6px}
.card--engine{left:250px;top:343px;width:140px;height:215px}
.card--engine h2{height:33px}
.card--engine .card-photo{background:linear-gradient(100deg,#a9b6c4,#e6ecf2 50%,#7c8a99)}
.card--engine .body{padding:5px 6px 0;font-size:8.8px;line-height:10.8px}
.card--team{left:395px;top:357px;width:122px;height:185px}
.card--team .card-photo{background:linear-gradient(90deg,#f2f2f2,#cfcfcf 50%,#f2f2f2)}
.card--team .body{padding:7px 12px}
.card--poll{left:520px;top:370px;width:105px;height:160px}
.card--poll .body{padding:5px 8px}
.poll-q{text-align:center;margin-bottom:5px}
.poll-option{display:flex;align-items:center;gap:14px;padding-left:10px;height:22px}
.radio{width:13px;height:13px;border-radius:50%;background:radial-gradient(circle at 40% 35%,#f4c3d0,#c8587a)}
.radio.is-checked{background:radial-gradient(circle at 40% 35%,#e2416c,#7a0026)}
.footer{left:0;top:567px;width:638px;height:30px;background:var(--blush);display:flex;align-items:center}
.footer-brand{margin-left:16px;color:var(--crimson);font-weight:700;font-size:19px;letter-spacing:-.5px;width:100px}
.footer-links{color:var(--crimson);font-weight:700;font-size:7.4px;line-height:10px}
.content{left:20px;top:115px;width:427px;height:437px;border-radius:7px;background:linear-gradient(#fafafa,#dedede);box-shadow:0 1px 4px rgba(0,0,0,.35)}
.content h1{height:37px;background:var(--crimson);color:#fff;font-size:15.5px;padding-left:20px;display:flex;align-items:center;border-radius:7px 7px 0 0}
.content .text{padding:6px 18px 0 20px;font-size:9.6px;line-height:15.1px}
.content .text p{margin-bottom:15px}
.sidebar{left:461px;top:115px;width:160px;height:292px;border-radius:7px;background:linear-gradient(#fafafa,#dedede);box-shadow:0 1px 4px rgba(0,0,0,.35)}
.sidebar h2{height:33px;background:var(--crimson);color:#fff;font-size:12.5px;display:flex;align-items:center;justify-content:center;border-radius:7px 7px 0 0}
.sidebar ul{list-style:none;padding-top:7px;font-size:9px;line-height:11px}
.sidebar li{padding:4px 14px;margin-bottom:3px}
.sidebar li.is-current{background:var(--crimson);color:#fff;padding:3px 14px}
.side-contact{left:461px;top:419px;width:160px;height:133px;border-radius:7px;background:linear-gradient(#fafafa,#dedede);box-shadow:0 1px 4px rgba(0,0,0,.35);font-size:10.5px;line-height:13px}
.side-contact .bar{height:30px;background:var(--crimson);border-radius:7px 7px 0 0}
.side-contact .body{padding:5px 0 0 21px}
.side-contact p{margin-bottom:10px}
</style>
</head>
<body>
<div class="stage">

  <section class="page page--home">
    <header class="masthead"></header>
    <div class="brand"><span class="brand-mark"></span>quenvora group</div>
    <nav class="nav">
      <a class="is-active">home</a><a>mortgage<br>solutions</a><a>messaging</a><a>company</a><a>news</a><a>support</a><a>privacy<br>policy</a><a>site<br>map</a><a>contact<br>us</a>
    </nav>
    <div class="hero">
      <div class="hero-photo" role="img" aria-label="Photo of three colleagues working together at an office computer"></div>
      <div class="hero-copy">
        <h1>Welcome to Quenvora</h1>
        <p>Quenvora is a leading software player in the Australian mortgage industry with over 10 years industry track record as a proven innovator.</p>
        <p>Our team of industry experts concentrate on accelerating your business goals and outcomes, offering a vendorindependent mix of business technology solutions customised to complement your key business processes.</p>
      </div>
    </div>

    <div class="card card--contact">
      <h2>Contact Us</h2>
      <div class="body">
        <p>Sales<br>02 8046 3120</p>
        <p>Support<br>1300 482 611</p>
        <p>Office Location<br>Level 14 62 Harlow St Eastbrook NSW 2071</p>
      </div>
    </div>

    <div class="card card--facts">
      <h2>Quick Facts</h2>
      <div class="card-photo" role="img" aria-label="Photo of business people sprinting on a running track"></div>
      <div class="body">
        <p>Set up and use in as little as 5 minutes</p>
        <p>Easy to learn intuitive design</p>
        <p>Incredibly fast and reliable</p>
      </div>
      <span class="more">+</span>
    </div>

    <div class="card card--engine">
      <h2>Product Engine</h2>
      <div class="card-photo" role="img" aria-label="Photo of a person walking past a modern glass building"></div>
      <div class="body">Product Engine is a web based tool that enables a loan writer to quickly create auditable, accountable assessment of products for their home loan customer. Being web-based it can be used anywhere, anytime and delivers significant value by</div>
      <span class="more">+</span>
    </div>

    <div class="card card--team">
      <h2>Support Team</h2>
      <div class="card-photo" role="img" aria-label="Photo of the support team standing in a row"></div>
      <div class="body">Fully supported by our friendly Sydney based support team from 8am – 7pm business days</div>
      <span class="more">+</span>
    </div>

    <div class="card card--poll">
      <h2>Poll</h2>
      <div class="body">
        <p class="poll-q">The question of<br>all questions?</p>
        <div class="poll-option"><span class="radio"></span>Question 1</div>
        <div class="poll-option"><span class="radio is-checked"></span>Question 2</div>
        <div class="poll-option"><span class="radio"></span>Question 3</div>
        <div class="poll-option"><span class="radio"></span>Question 4</div>
      </div>
    </div>

    <footer class="footer">
      <span class="footer-brand">quenvora</span>
      <div class="footer-links">Sales Platform | e-app | Product Engine | Calculations | Commissions | Messaging | IT Services | Support | Company | News | Contact<br>© 2009, Quenvora Group Inc. All rights reserved.</div>
    </footer>
  </section>

  <div class="divider"></div>

  <section class="page page--crm">
    <header class="masthead"></header>
    <div class="brand"><span class="brand-mark"></span>quenvora group</div>
    <nav class="nav">
      <a>home</a><a class="is-active">mortgage<br>solutions</a><a>messaging</a><a>company</a><a>news</a><a>support</a><a>privacy<br>policy</a><a>site<br>map</a><a>contact<br>us</a>
    </nav>

    <article class="content">
      <h1>CRM (Sales Platform)</h1>
      <div class="text">
        <p>Quenvora Group of companies has more than 21 years of experience delivering technology based business solutions to Australia's leading firms. We understand that success is not just based on a smart strategy; but that it comes with a pragmatic focus on achievable results. Our team of industry experts concentrate on accelerating your business goals and outcomes, offering a vendorindependent mix of business technology solutions customised to complement your key business processes. The result is a measurable contribution of innovation and new value across your organisation. The Quenvora Group solutions heritage includes complete and customised business transaction platforms, all the way through to building secure and flexible IT infrastructures. We can even run and manage your entire IT systems and services for you if required.</p>
        <p>Quenvora Group of companies has more than 21 years of experience delivering technology based business solutions to Australia's leading firms. We understand that success is not just based on a smart strategy; but that it comes with a pragmatic focus on achievable results. Our team of industry experts concentrate on accelerating your business goals and outcomes, offering a vendorindependent mix of business technology solutions customised to complement your key business processes. The result is a measurable contribution of innovation and new value across your organisation. The Quenvora Group solutions heritage includes complete and customised business transaction platforms, all the way through to building secure and flexible IT infrastructures. We can even run and manage your entire IT systems and services for you if required.</p>
        <p>Quenvora Group of companies has more than 21 years of experience delivering technology based business solutions to Australia's leading firms. We understand that success is not just based on a smart strategy; but that it comes with a pragmatic focus on achievable results.</p>
      </div>
    </article>

    <aside class="sidebar">
      <h2>Mortgage Solutions</h2>
      <ul>
        <li class="is-current">CRM (Sales Platform)</li>
        <li>Commission Processing</li>
        <li>Electronic Lodgement (E-App)<br>and Application Tracking</li>
        <li>Mortgage Product Search<br>and Compare (Product Engine)</li>
        <li>Mortgage Calculators</li>
        <li>Competition page</li>
        <li>The Mortgage Business Team<br>(Team information)</li>
        <li>Quenvora Partners</li>
        <li>Technical Support &nbsp;and FAQ</li>
        <li>News/Blog</li>
      </ul>
    </aside>

    <aside class="side-contact">
      <div class="bar"></div>
      <div class="body">
        <p>Sales: 02 8046 3120</p>
        <p>Support: 1300 482 611</p>
        <p>Office Location<br>Level 14 62 Harlow St<br>Eastbrook NSW 2071</p>
      </div>
    </aside>

    <footer class="footer">
      <span class="footer-brand">quenvora</span>
      <div class="footer-links">Sales Platform | e-app | Product Engine | Calculations | Commissions | Messaging | IT Services | Support | Company | News | Contact<br>© 2009, Quenvora Group Inc. All rights reserved.</div>
    </footer>
  </section>

</div>
</body>
</html>
```